Need a sleek, professional business card design for a Web Development business

I need a unique business card designed for a web development company. It is also the parent company for any ventures I do, such as my ClipWave channel, startup ideas I have, etc. I am the single member of "Bright Harbor Code LLC." I will attach my basic logo here, so you will see the current color scheme and have the asset available. Thank you!

Target Market(s)

Startups, SMB's, Professionals

Industry/Entity Type

Business

Font styles to use
Other font styles liked:
• Lovello for headings is what I use, but not necessary.

Colors

Designer to choose colors to be used in the design.

Requirements
Nice to have
• Sleek is the word. Professional, modern, dark.
Should not have
• Any work from someone else's design. Lacking originality.

```html
<!DOCTYPE html>
<html lang="en">
<head>
<meta charset="utf-8">
<title>Bright Harbor Code LLC — Business Card</title>
<link rel="stylesheet" href="https://fonts.googleapis.com/css2?family=Roboto+Slab:wght@800&family=Open+Sans:wght@300;400&display=swap">
<style>
  :root {
    --bg-light: #e4e4e4;
    --bg-dark: #b9b9b9;
    --card: #141414;
    --coral: #ea5f68;
    --coral-soft: #f08a6a;
    --peach: #f6a862;
    --white: #ffffff;
    --muted: #e6e6e6;
  }
  * { margin: 0; padding: 0; box-sizing: border-box; }
  html, body { width: 1200px; height: 1200px; overflow: hidden; }
  body {
    background: radial-gradient(circle at 30% 70%, var(--bg-light), var(--bg-dark));
    font-family: "Open Sans", sans-serif;
    position: relative;
  }
  .card {
    position: absolute;
    left: 150px;
    width: 900px;
    height: 514px;
    background: var(--card);
    box-shadow: 0 14px 30px rgba(0,0,0,.28);
    overflow: hidden;
  }
  .card--front { top: 48px; }
  .card--back { top: 630px; }

  .brand {
    position: absolute;
    display: flex;
    flex-direction: column;
    align-items: center;
  }
  .brand__mark {
    border-radius: 22%;
    background: linear-gradient(180deg, var(--coral), var(--peach));
  }
  .brand__name {
    font-family: "Roboto Slab", serif;
    font-weight: 800;
    color: var(--white);
    white-space: nowrap;
  }
  .card--front .brand { left: 0; right: 0; top: 128px; }
  .card--front .brand__mark { width: 150px; height: 150px; margin-bottom: 34px; }
  .card--front .brand__name { font-size: 30px; }

  .card--back .brand { left: 40px; width: 380px; top: 110px; }
  .card--back .brand__mark { width: 210px; height: 210px; margin-bottom: 40px; }
  .card--back .brand__name { font-size: 32px; }

  .profile {
    position: absolute;
    right: 250px;
    top: 58px;
    text-align: right;
  }
  .profile__name {
    font-weight: 300;
    font-size: 44px;
    color: var(--coral);
    line-height: 1;
  }
  .profile__role {
    font-size: 17px;
    color: var(--muted);
    margin-top: 4px;
  }
  .contact {
    position: absolute;
    top: 164px;
    right: 0;
    width: 640px;
    list-style: none;
  }
  .contact__row {
    display: flex;
    align-items: center;
    justify-content: flex-end;
    height: 50px;
  }
  .contact__text {
    font-size: 17px;
    color: var(--muted);
    text-align: right;
    line-height: 1.35;
    margin-right: 22px;
  }
  .contact__bar {
    width: 220px;
    height: 24px;
    background: var(--coral);
    display: flex;
    align-items: center;
    padding-left: 8px;
  }
  .contact__bar svg { width: 14px; height: 14px; fill: var(--white); }
</style>
</head>
<body>

<section class="card card--front">
  <div class="brand">
    <div class="brand__mark"></div>
    <div class="brand__name">Bright Harbor Code LLC</div>
  </div>
</section>

<section class="card card--back">
  <div class="brand">
    <div class="brand__mark"></div>
    <div class="brand__name">Bright Harbor Code LLC</div>
  </div>

  <div class="profile">
    <div class="profile__name">Your Name</div>
    <div class="profile__role">Designation</div>
  </div>

  <ul class="contact">
    <li class="contact__row">
      <span class="contact__text">Lorem Ipsum is simply<br>dummy text of the printing and</span>
      <span class="contact__bar"><svg viewBox="0 0 24 24"><path d="M12 2a7 7 0 0 0-7 7c0 5 7 13 7 13s7-8 7-13a7 7 0 0 0-7-7zm0 9.5A2.5 2.5 0 1 1 12 6.5a2.5 2.5 0 0 1 0 5z"/></svg></span>
    </li>
    <li class="contact__row">
      <span class="contact__text">+91 1234567890</span>
      <span class="contact__bar"><svg viewBox="0 0 24 24"><path d="M6.6 10.8a15 15 0 0 0 6.6 6.6l2.2-2.2c.3-.3.7-.4 1-.2 1.1.4 2.3.6 3.6.6.6 0 1 .4 1 1V20c0 .6-.4 1-1 1A17 17 0 0 1 3 4c0-.6.4-1 1-1h3.5c.6 0 1 .4 1 1 0 1.3.2 2.5.6 3.6.1.3 0 .7-.2 1z"/></svg></span>
    </li>
    <li class="contact__row">
      <span class="contact__text">+91 1234567890</span>
      <span class="contact__bar"><svg viewBox="0 0 24 24"><path d="M7 1h10a2 2 0 0 1 2 2v18a2 2 0 0 1-2 2H7a2 2 0 0 1-2-2V3a2 2 0 0 1 2-2zm0 3v14h10V4zm5 15.5a1 1 0 1 0 0 2 1 1 0 0 0 0-2z"/></svg></span>
    </li>
    <li class="contact__row">
      <span class="contact__text">+91 1234567890</span>
      <span class="contact__bar"><svg viewBox="0 0 24 24"><path d="M6 2h9v6H6zM3 9h18v13H3zm3 3v2h3v-2zm5 0v2h3v-2zm5 0v2h3v-2zm-10 4v2h3v-2zm5 0v2h3v-2z"/></svg></span>
    </li>
    <li class="contact__row">
      <span class="contact__text">info@brightharborcode.com</span>
      <span class="contact__bar"><svg viewBox="0 0 24 24"><path d="M2 5h20v14H2zm2 2v.5l8 5 8-5V7l-8 5z"/></svg></span>
    </li>
    <li class="contact__row">
      <span class="contact__text">www.brightharborcode.com</span>
      <span class="contact__bar"><svg viewBox="0 0 24 24"><path d="M12 2a10 10 0 1 0 0 20 10 10 0 0 0 0-20zm6.9 6h-3a15 15 0 0 0-1.3-3.9A8 8 0 0 1 18.9 8zM12 4c.8 1.2 1.5 2.5 1.9 4h-3.8c.4-1.5 1.1-2.8 1.9-4zM4.3 14a8 8 0 0 1 0-4h3.4a16 16 0 0 0 0 4zm.8 2h3a15 15 0 0 0 1.3 3.9A8 8 0 0 1 5.1 16zm3-8h-3a8 8 0 0 1 4.3-3.9C8.8 5.3 8.4 6.6 8.1 8zM12 20c-.8-1.2-1.5-2.5-1.9-4h3.8c-.4 1.5-1.1 2.8-1.9 4zm2.3-6H9.7a14 14 0 0 1 0-4h4.6a14 14 0 0 1 0 4zm.3 5.9c.6-1.2 1-2.5 1.3-3.9h3a8 8 0 0 1-4.3 3.9zm1.7-5.9a16 16 0 0 0 0-4h3.4a8 8 0 0 1 0 4z"/></svg></span>
    </li>
  </ul>
</section>

</body>
</html>
```